PFM Web Design Project

I'm looking for a small, friendly,functional, information based website. If you go through the attachments, you would know the nature of the business.
Updates

Hi,

I have uploaded a picture of the CEO, Mr. Rafael Okonto DPAMV member. Please feel free to use it whereever appropriate.

Thanks!

Reason: Still not satisfied with the designs. Waiting to get layouts from top designers invited to the project.

Hello, I have uploaded some references. I like the colours used on the bar and would w

Example of a we page . I like this layout for the inside pages.

I am changing the tabs on my website to:

Home
About us
Services
Contact us

The services tab will have three sub pages:

Immigration
Education
AccommodationAccommodation

Target Market(s)

Young international students willing to come to Canada to study, young international students willing to immigrate to Canada, parents of the students

Industry/Entity Type

Business

Requirements
Must have
• PFM HOME
ABOUT US
CONTACT
SERVICES
TAG LINE

The website should look n feel trendy, smart, current, factual, trustworthy etc....
Nice to have
• I am looking for a bold, attractive, eye catchy home page with less text! Something that makes a statement....
Should not have
• No Clip art, flash animation, no bells n whistles please

```html
<!DOCTYPE html>
<html lang="en">
<head>
<meta charset="utf-8">
<title>PFM – Dare to Dream Canadian</title>
<link rel="stylesheet" href="https://fonts.googleapis.com/css2?family=Mulish:wght@600;800&family=PT+Sans:wght@400;700&family=Ubuntu:wght@700&display=swap">
<style>
  :root{
    --red:#ee0000;
    --red-deep:#d40000;
    --red-light:#ff2a2a;
    --page-top:#d3d3d3;
    --page-bottom:#e8e8e8;
    --white:#ffffff;
    --panel:#efefef;
    --rule:#555555;
    --ink:#111111;
    --text:#777777;
    --nav-text:#6d6d6d;
    --brand-grey:#8c8c8c;
  }
  *{margin:0;padding:0;box-sizing:border-box}
  html,body{width:1200px;height:750px;overflow:hidden}
  body{
    background:linear-gradient(var(--page-top) 0 187px,var(--page-bottom) 187px);
    font-family:"PT Sans",sans-serif;
    position:relative;
  }
  .site{position:absolute;left:172px;top:0;width:842px;height:750px;background:var(--white);overflow:hidden}
  .topbar{position:absolute;left:0;top:0;width:100%;height:15px;background:linear-gradient(var(--red-light),var(--red-deep));z-index:1}

  .brand{position:absolute;left:28px;top:44px;display:flex;align-items:center;gap:12px;color:var(--brand-grey);font-family:"PT Sans",sans-serif;font-weight:700}
  .brand-mark{width:34px;height:34px;background:var(--red)}
  .brand-name{display:flex;flex-direction:column;line-height:1}
  .brand-name .short{font-size:46px;letter-spacing:1px}
  .brand-name .long{font-size:18px;margin-top:4px}

  .tagline{position:absolute;left:253px;top:72px;z-index:2;white-space:nowrap;font-family:"Mulish",sans-serif;font-weight:800;font-size:21px;color:var(--red)}

  .hero-photo{position:absolute;left:536px;top:9px;width:300px;height:178px;z-index:0;
    background:linear-gradient(180deg,#f4f4f4 0%,#cfcfcf 35%,#3a3a3a 70%,#1c1c1c 100%)}

  .main-nav{position:absolute;left:0;top:153px;width:100%;height:34px;z-index:3;
    background:linear-gradient(rgba(250,250,250,.82),rgba(225,225,225,.82))}
  .main-nav a{position:absolute;top:0;height:34px;line-height:34px;text-decoration:none;white-space:nowrap;
    font-family:"Mulish",sans-serif;font-weight:600;font-size:15px;color:var(--nav-text);transform:translateX(-50%)}
  .main-nav a.is-active{left:0;width:137px;transform:none;text-align:center;color:var(--white);
    background:linear-gradient(var(--red-light),var(--red-deep))}

  .feature{position:absolute;top:0}
  .feature h2{position:absolute;font-family:"Ubuntu",sans-serif;font-weight:700;font-size:13.5px;color:var(--ink);white-space:nowrap}
  .feature .photo{position:absolute;left:0}
  .feature p{position:absolute;left:0;font-size:12px;color:var(--text)}
  .btn{position:absolute;left:0;width:100px;height:29px;line-height:29px;text-align:center;color:var(--white);
    font-size:13px;text-decoration:none;border-radius:2px;
    background:linear-gradient(var(--red-light),var(--red-deep));box-shadow:0 1px 2px rgba(0,0,0,.35)}

  .mission{position:absolute;left:0;top:555px;width:100%;height:148px;background:var(--panel)}
  .mission h2{position:absolute;left:47px;top:34px;font-family:"Ubuntu",sans-serif;font-weight:700;font-size:13.5px;color:var(--ink)}
  .mission p{position:absolute;left:47px;top:63px;width:742px;font-size:12px;line-height:17px;color:var(--text)}

  .footer{position:absolute;left:0;top:703px;width:100%;height:47px;border-top:4px solid var(--rule);
    background:linear-gradient(var(--red-deep),var(--red))}
  .footer nav{position:absolute;top:25px;width:100%;text-align:center;font-size:11px;color:var(--white)}
  .footer a{color:var(--white);text-decoration:none;margin:0 8px}
</style>
</head>
<body>
<div class="site">
  <div class="topbar"></div>

  <header>
    <div class="brand">
      <span class="brand-mark"></span>
      <span class="brand-name"><span class="short">PFM</span><span class="long">Prairie Frontier Management</span></span>
    </div>
    <div class="hero-photo" role="img" aria-label="Group of cheering graduates in black gowns and caps"></div>
    <div class="tagline">Dare to Dream Canadian...</div>
  </header>

  <nav class="main-nav">
    <a class="is-active" href="#">HOME</a>
    <a href="#" style="left:218px">ABOUT US</a>
    <a href="#" style="left:378px">SERVICES</a>
    <a href="#" style="left:547px">PFM MISSION</a>
    <a href="#" style="left:729px">CONTACT US</a>
  </nav>

  <section class="feature" style="left:47px">
    <h2 style="top:221px">IMMIGRATION</h2>
    <div class="photo" role="img" aria-label="Smiling family outdoors" style="top:248px;width:199px;height:135px;background:linear-gradient(135deg,#c9d6b8,#e6d2c0 50%,#8a9b6c)"></div>
    <p style="top:398px;width:198px;line-height:17px">Canada has been consistently rated by the World Living Council as one of the top countries in the world to live, work .......</p>
    <a class="btn" href="#" style="top:477px">Read More</a>
  </section>

  <section class="feature" style="left:318px">
    <h2 style="top:221px">EDUCATION</h2>
    <div class="photo" role="img" aria-label="Graduate in cap holding a diploma" style="top:248px;width:205px;height:139px;background:linear-gradient(90deg,#d8dde0,#efe4dc 45%,#2a2a2a 80%,#cfd6da)"></div>
    <p style="top:401px;width:185px;line-height:19px">Canada has one of the finest education systems in the world. Every year thousands of students from all over the world .......</p>
    <a class="btn" href="#" style="top:487px">Read More</a>
  </section>

  <section class="feature" style="left:595px">
    <h2 style="top:221px">STUDENT ACCOMODATION</h2>
    <div class="photo" role="img" aria-label="Apartment buildings seen from below against a blue sky" style="top:250px;width:204px;height:135px;background:radial-gradient(circle at 45% 40%,#7fa9d6 0,#9bb9d8 25%,#9a948a 50%,#5e5a54 100%)"></div>
    <p style="top:405px;width:200px;line-height:17px">We have assisted<br>many international students find a home away from home in Canada. International students .......</p>
    <a class="btn" href="#" style="top:485px">Read More</a>
  </section>

  <section class="mission">
    <h2>PFM MISSION</h2>
    <p>At PFM we are committed to our customer centered philosophy. Our mission is to help our clients achieve their goals by providing them with world class customer service that is both reliable and competitively superior. We are driven by our core values: ethics, expertise and leadership. We believe that honesty paves the way for true success. We have been there. We know what it takes.</p>
  </section>

  <footer class="footer">
    <nav><a href="#">Privacy Policy</a>|<a href="#">Terms Of Use</a>|<a href="#">Feedback</a></nav>
  </footer>
</div>
</body>
</html>
```